business card design for velmora textile printing

Velmora Textile Printing requires elegant and colorful designs for its business card, ensuring both are visually cohesive and reflect the brand’s creative, modern identity. The logo is already finalized and should be a central element in designs.

## Business Card Design Brief

- Feature the logo clearly, with colors and style matching the letterhead.
- Present contact information (name, title, phone, email, website, address) in a clear, organized manner.
- Open to creative layouts, finishes, and double-sided designs, as long as the card remains professional and easy to read.
- Ensure both pieces feel unified as part of the same brand identity.

The final designs should be vibrant, professional, and memorable, showcasing Velmora Textile Printing’s creative spirit.

Target Market(s)

Pakistan

Industry/Entity Type

Textile printing

Other font styles liked:
• Calibri

Requirements
Must have
• Address Email Address Phone number designer can ask me when start designing

```html
<!DOCTYPE html>
<html lang="en">
<head>
<meta charset="UTF-8">
<title>Velmora Textile Printing – Business Card</title>
<link rel="stylesheet" href="https://fonts.googleapis.com/css2?family=Carlito:wght@400;700&display=swap">
<style>
  :root {
    --backdrop: #2e2e30;
    --maroon: #632224;
    --paper: #ffffff;
    --orange: #f2611f;
    --magenta: #a3169a;
    --ink: #3a3a3a;
    --rule: #8a3b36;
    --purple: #7a2a9a;
  }
  * { box-sizing: border-box; margin: 0; padding: 0; }
  html, body {
    width: 1200px; height: 875px; overflow: hidden;
    background: var(--backdrop);
    font-family: "Carlito", Calibri, Arial, sans-serif;
  }
  .stage {
    width: 1200px; height: 875px;
    display: flex; align-items: center; justify-content: center; gap: 40px;
  }
  .card {
    width: 540px; height: 310px; border-radius: 18px;
    position: relative; overflow: hidden;
  }
  .card--front { background: var(--maroon); }
  .card--back { background: var(--paper); }

  .brand {
    position: absolute; display: flex; flex-direction: column; align-items: center;
  }
  .brand__dot { border-radius: 50%; background: var(--orange); }
  .brand__name { font-weight: 700; text-transform: uppercase; text-align: center; line-height: 1.05; }

  .card--front .brand { left: 0; right: 0; top: 82px; gap: 16px; }
  .card--front .brand__dot { width: 64px; height: 64px; }
  .card--front .brand__name { color: var(--paper); font-size: 30px; letter-spacing: 3px; }
  .card--front .brand__name span { display: block; font-size: 17px; letter-spacing: 4px; }

  .card--back .brand { left: 255px; top: 36px; width: 200px; gap: 10px; }
  .card--back .brand__dot { width: 46px; height: 46px; }
  .card--back .brand__name { color: var(--maroon); font-size: 21px; letter-spacing: 2px; }
  .card--back .brand__name span { display: block; font-size: 12px; letter-spacing: 3px; }

  .person { position: absolute; right: 310px; top: 168px; text-align: right; }
  .person__name { font-size: 27px; font-weight: 700; letter-spacing: .5px; }
  .person__first { color: var(--orange); }
  .person__last { color: var(--magenta); }
  .person__title { font-size: 15px; color: var(--ink); margin-top: 2px; }

  .divider { position: absolute; left: 246px; top: 160px; width: 1.5px; height: 70px; background: var(--rule); }

  .contacts { position: absolute; left: 262px; top: 158px; list-style: none; }
  .contacts li { display: flex; align-items: center; gap: 8px; font-size: 14px; color: var(--ink); line-height: 24px; }
  .contacts svg { width: 13px; height: 13px; flex: none; }

  .address { position: absolute; left: 0; right: 0; bottom: 30px; text-align: center; font-size: 14px; color: var(--ink); }
</style>
</head>
<body>
<main class="stage">
  <section class="card card--front" aria-label="Card front">
    <div class="brand">
      <div class="brand__dot"></div>
      <p class="brand__name">Velmora<span>Textile Printing</span></p>
    </div>
  </section>

  <section class="card card--back" aria-label="Card back">
    <div class="brand">
      <div class="brand__dot"></div>
      <p class="brand__name">Velmora<span>Textile Printing</span></p>
    </div>

    <div class="person">
      <p class="person__name"><span class="person__first">DANIEL</span> <span class="person__last">HAYES</span></p>
      <p class="person__title">CEO/Founder</p>
    </div>

    <div class="divider"></div>

    <ul class="contacts">
      <li>
        <svg viewBox="0 0 24 24"><path fill="#f2611f" d="M6.6 10.8a15 15 0 0 0 6.6 6.6l2.2-2.2c.3-.3.7-.4 1-.2 1.1.4 2.3.6 3.6.6.6 0 1 .4 1 1V20c0 .6-.4 1-1 1A17 17 0 0 1 3 4c0-.6.4-1 1-1h3.5c.6 0 1 .4 1 1 0 1.3.2 2.5.6 3.6.1.3 0 .7-.2 1z"/></svg>
        (123) 555-0148
      </li>
      <li>
        <svg viewBox="0 0 24 24"><rect x="2" y="5" width="20" height="14" rx="1.5" fill="#a3169a"/><path d="M3 6l9 7 9-7" fill="none" stroke="#fff" stroke-width="1.6"/></svg>
        info@velmoratextileprinting.com
      </li>
      <li>
        <svg viewBox="0 0 24 24" fill="none" stroke="#7a2a9a" stroke-width="1.8"><circle cx="12" cy="12" r="9.5"/><ellipse cx="12" cy="12" rx="4" ry="9.5"/><path d="M2.5 12h19M4 7h16M4 17h16"/></svg>
        www.velmoratextileprinting.com
      </li>
    </ul>

    <p class="address">5678 Market Street, Suite #4410 Country Name, AB 54021</p>
  </section>
</main>
</body>
</html>
```